Vision / Mission Poster Required

We are looking to display our company Vision / Mission / Values on a poster. This will be displayed in the head office and other site offices.

The document needs to look professional however still be fun, eye catching and easy to read. It will be predominantly displayed in A3 format.

The design needs to use our company Logo which is attached along with the Text to display on the poster. I have put some additional text on the doc that you can include if it suits the layout but is not essential.

Target Market(s)

Staff, Corporate Visitors

Industry/Entity Type

Electric Company

Font styles to use
Sans Serif

Colors

Designer to choose colors to be used in the design.

Requirements
Must have
• Incorporate Logo
• Professional Look
• Attention grabbing
• Easy to Read
Should not have
• Lightning Bolts
• Pictures of random people/Things

```html
<!DOCTYPE html>
<html lang="en">
<head>
<meta charset="utf-8">
<title>Brightline Electrical Services — Vision, Mission, Values</title>
<link rel="stylesheet" href="https://fonts.googleapis.com/css2?family=Montserrat:wght@600;700;800&family=Roboto+Condensed:wght@300;700&family=Open+Sans:wght@400;600&display=swap">
<style>
  :root {
    --blue: #1f4e8c;
    --navy: #17386e;
    --orange: #f26b1d;
    --text: #333a44;
    --grey: #5a5f66;
    --rule: #9aa0a8;
    --page: #ececec;
    --paper: #ffffff;
  }
  * { box-sizing: border-box; margin: 0; padding: 0; }
  html, body { width: 1200px; height: 1200px; overflow: hidden; }
  body { background: var(--page); font-family: "Open Sans", Arial, sans-serif; color: var(--text); }

  .poster {
    position: absolute; left: 197px; top: 30px;
    width: 806px; height: 1140px;
    background: var(--paper); overflow: hidden;
    box-shadow: 0 12px 40px rgba(0,0,0,.12);
  }
  .poster-shapes { position: absolute; inset: 0; }

  .brand { position: absolute; left: 52px; top: 160px; display: flex; align-items: center; gap: 14px; }
  .brand-dot { width: 40px; height: 40px; border-radius: 50%; background: var(--orange); }
  .brand-name { font-family: "Montserrat", sans-serif; font-weight: 800; font-size: 34px; color: var(--blue); letter-spacing: .5px; }

  .section-label {
    font-family: "Montserrat", sans-serif; font-weight: 700; color: var(--orange);
    text-transform: uppercase; letter-spacing: 1px;
  }
  .vision-label {
    position: absolute; left: 52px; top: 300px; width: 200px;
    font-size: 38px; padding: 12px 0;
    border-top: 1px solid var(--rule); border-bottom: 1px solid var(--rule);
  }
  .vision-statement {
    position: absolute; left: 52px; top: 410px; width: 350px;
    font-family: "Roboto Condensed", sans-serif; font-weight: 300;
    color: var(--navy); font-size: 34px; line-height: 1.05; text-transform: uppercase;
  }
  .vision-statement strong { font-weight: 700; color: var(--grey); }
  .vision-statement .accent { display: block; font-family: "Montserrat", sans-serif; font-weight: 800; color: var(--orange); font-size: 44px; }

  .column { position: absolute; }
  .mission { left: 52px; top: 620px; width: 350px; }
  .values { left: 430px; top: 525px; width: 340px; }
  .column .section-label {
    font-size: 16px; padding-bottom: 6px; margin-bottom: 12px;
    border-bottom: 1.5px solid var(--orange);
  }
  .item { margin-bottom: 10px; }
  .mission .item { margin-bottom: 20px; }
  .pill {
    display: inline-block; background: var(--navy); color: #fff;
    font-family: "Montserrat", sans-serif; font-weight: 600; font-size: 11px;
    text-transform: uppercase; letter-spacing: .3px;
    padding: 3px 12px; border-radius: 10px; margin-bottom: 4px;
  }
  .item p { font-size: 10.5px; line-height: 1.35; color: var(--text); }

  .contact {
    position: absolute; left: 78px; top: 1000px; color: #fff;
    font-family: "Open Sans", sans-serif; font-weight: 600; font-size: 19px; line-height: 1.3;
  }
  .contact li { list-style: none; display: flex; align-items: flex-start; gap: 12px; margin-bottom: 8px; }
  .contact svg { flex: none; margin-top: 5px; }
</style>
</head>
<body>
<main class="poster">
  <svg class="poster-shapes" width="806" height="1140" viewBox="0 0 806 1140">
    <circle cx="600" cy="265" r="238" fill="none" stroke="var(--orange)" stroke-width="14"/>
    <circle cx="605" cy="262" r="212" fill="none" stroke="var(--navy)" stroke-width="12"/>
    <circle cx="605" cy="262" r="204" fill="#b9c6d3" role="img" aria-label="Photo of a bright modern open-plan office with ceiling lights and blue chairs"/>
    <circle cx="745" cy="1080" r="125" fill="none" stroke="var(--orange)" stroke-width="10"/>
    <circle cx="745" cy="1080" r="114" fill="none" stroke="var(--navy)" stroke-width="8"/>
    <circle cx="745" cy="1080" r="108" fill="#d9cfc2" role="img" aria-label="Photo of an elegant chandelier in a dining room"/>
    <circle cx="565" cy="1070" r="68" fill="none" stroke="var(--orange)" stroke-width="8"/>
    <circle cx="565" cy="1070" r="59" fill="none" stroke="var(--navy)" stroke-width="7"/>
    <circle cx="565" cy="1070" r="54" fill="#6f8fb8" role="img" aria-label="Photo of a hand holding a screwdriver at a switchboard"/>
    <circle cx="230" cy="1240" r="300" fill="none" stroke="var(--orange)" stroke-width="14"/>
    <circle cx="230" cy="1240" r="282" fill="var(--blue)"/>
  </svg>

  <div class="brand">
    <span class="brand-dot"></span>
    <span class="brand-name">BRIGHTLINE</span>
  </div>

  <h2 class="section-label vision-label">Vision:</h2>
  <p class="vision-statement">To be Perth’s <strong>premier provider</strong> of electrical service <span class="accent">Solutions</span></p>

  <section class="column mission">
    <h3 class="section-label">Mission:</h3>
    <div class="item">
      <span class="pill">Deliver growth and value</span>
      <p>Maintaining a market presence – Leveraging our technical resources – Networking and developing stakeholder relationships</p>
    </div>
    <div class="item">
      <span class="pill">Remain profitable</span>
      <p>Increasing revenue – Optimizing capacity utilization – Maintaining expenses</p>
    </div>
    <div class="item">
      <span class="pill">Be sustainable</span>
      <p>Improving internal efficiency – Diversifying our income sources – Implementing Social &amp; Environmental improvement initiatives</p>
    </div>
  </section>

  <section class="column values">
    <h3 class="section-label">Values:</h3>
    <div class="item">
      <span class="pill">Honesty &amp; integrity</span>
      <p>Customers, contractors and suppliers will be able to count on Brightline personnel to deal straightforwardly and adhere to the strictest moral and ethical codes of conduct.</p>
    </div>
    <div class="item">
      <span class="pill">Safety &amp; responsibility</span>
      <p>Brightline is committed to constantly improving safety practices at project job sites and within the electrical service industry as a whole.</p>
    </div>
    <div class="item">
      <span class="pill">Commitment to quality</span>
      <p>Customers and stakeholders will be able to count on Brightline’s workmanship being among the best in the industry.</p>
    </div>
    <div class="item">
      <span class="pill">Innovation &amp; technology</span>
      <p>Customers can rely on us to apply the latest proven technologies on their projects, and to be on the ground floor of industry standards for new and emerging markets.</p>
    </div>
    <div class="item">
      <span class="pill">Knowledgeable &amp; valued employees</span>
      <p>Brightline recognizes that its greatest asset is its people. We pledge to treat each employee with integrity, dealing honestly with all.</p>
    </div>
  </section>

  <ul class="contact">
    <li>
      <svg width="18" height="18" viewBox="0 0 18 18"><circle cx="9" cy="9" r="8" fill="none" stroke="#fff" stroke-width="1.6"/><rect x="4.5" y="6" width="9" height="6" fill="none" stroke="#fff" stroke-width="1.2"/><path d="M4.5 6 9 9.5 13.5 6" fill="none" stroke="#fff" stroke-width="1.2"/></svg>
      <span>info@brightline-es.com.au</span>
    </li>
    <li>
      <svg width="18" height="18" viewBox="0 0 18 18"><path d="M2 9 9 3l7 6M4.5 7.5V15h9V7.5" fill="none" stroke="#fff" stroke-width="1.8"/></svg>
      <span>12 Harlow Street<br>East Perth WA 6004</span>
    </li>
    <li>
      <svg width="18" height="18" viewBox="0 0 18 18"><circle cx="9" cy="9" r="7.5" fill="none" stroke="#fff" stroke-width="1.5"/><ellipse cx="9" cy="9" rx="3.2" ry="7.5" fill="none" stroke="#fff" stroke-width="1.2"/><path d="M1.5 9h15" stroke="#fff" stroke-width="1.2"/></svg>
      <span>www.brightline-es.com.au</span>
    </li>
  </ul>
</main>
</body>
</html>
```